Boat business cards

I'm looking for business cards with the two logos I've attached. I don't have an specific idea in mind and open to anything. All the usual info will be on the card. Name, position in company, nr, email, address, ect. The company rents out these two boats for charters and fishing.

```html
<!DOCTYPE html>
<html lang="en">
<head>
<meta charset="utf-8">
<title>Charter Business Cards</title>
<link rel="stylesheet" href="https://fonts.googleapis.com/css2?family=Arimo:wght@400;700&display=swap">
<style>
  :root{
    --page:#2b2b2d;
    --front-top:#ffffff;
    --front-bottom:#b9c6e4;
    --ink-grey:#6f7278;
    --card-black:#0d0d0e;
    --card-black-2:#262628;
    --gold:#b7966a;
    --white:#f2f2f2;
    --rule:#8a8a8a;
  }
  *{box-sizing:border-box;margin:0;padding:0}
  html,body{width:1200px;height:1023px;overflow:hidden}
  body{
    background:var(--page);
    font-family:"Arimo",Arial,sans-serif;
    display:flex;flex-direction:column;align-items:center;justify-content:center;gap:56px;
  }
  .card{
    width:760px;height:434px;border-radius:34px;position:relative;overflow:hidden;
    box-shadow:0 18px 40px rgba(0,0,0,.45);
  }
  /* front */
  .card--front{
    background:linear-gradient(180deg,var(--front-top) 0%,var(--front-top) 40%,var(--front-bottom) 100%);
    display:flex;flex-direction:column;align-items:center;justify-content:center;gap:18px;
  }
  .front__art{
    width:330px;height:150px;border-radius:10px;
    background:linear-gradient(160deg,#e9edf4 0%,#a9c3e6 70%,#8fb0dc 100%);
  }
  .front__name{
    font-size:58px;font-weight:700;color:var(--ink-grey);letter-spacing:1px;
  }
  /* back */
  .card--back{
    background:linear-gradient(135deg,var(--card-black-2) 0%,var(--card-black) 45%,var(--card-black) 100%);
    color:var(--white);
  }
  .back__brand{
    position:absolute;left:330px;top:48px;width:380px;
    display:flex;flex-direction:column;align-items:center;gap:14px;
  }
  .back__art{
    width:300px;height:120px;border-radius:8px;
    background:linear-gradient(180deg,#e8e8e8 0%,#b7966a 60%,#4a6a9a 100%);
  }
  .back__name{font-size:40px;font-weight:700;color:var(--white);letter-spacing:1px}
  .back__rule{
    position:absolute;left:300px;right:40px;top:282px;height:2px;background:var(--rule);
  }
  .back__address{
    position:absolute;right:46px;top:306px;text-align:right;font-size:24px;line-height:1.3;color:var(--white);
  }
  .back__person{position:absolute;left:44px;bottom:40px}
  .person__name{font-size:32px;font-weight:700;color:var(--gold)}
  .person__role{font-size:22px;color:var(--white);margin-top:4px}
  .person__rule{width:240px;height:2px;background:var(--rule);margin:12px 0 12px}
  .contact{list-style:none;display:flex;flex-direction:column;gap:8px}
  .contact__item{display:flex;align-items:center;gap:12px;font-size:22px;color:var(--white)}
  .contact__icon{width:26px;height:26px;flex:none}
</style>
</head>
<body>

<section class="card card--front" aria-label="Card front">
  <div class="front__art" role="img" aria-label="Line drawing of a sport-fishing boat"></div>
  <div class="front__name">Bora Bay</div>
</section>

<section class="card card--back" aria-label="Card back">
  <div class="back__brand">
    <div class="back__art" role="img" aria-label="Illustration of a motor yacht on water"></div>
    <div class="back__name">Harbor Tide</div>
  </div>
  <div class="back__rule"></div>
  <p class="back__address">Your address, city<br>state, ZIP 0000</p>

  <div class="back__person">
    <div class="person__name">Jonathan Smith</div>
    <div class="person__role">Manager</div>
    <div class="person__rule"></div>
    <ul class="contact">
      <li class="contact__item">
        <svg class="contact__icon" viewBox="0 0 26 26"><rect width="26" height="26" rx="5" fill="#b7966a"/><path d="M8 6l3 3-2 2a9 9 0 0 0 6 6l2-2 3 3-2 2c-6 0-12-6-12-12z" fill="#0d0d0e"/></svg>
        123-456-2100
      </li>
      <li class="contact__item">
        <svg class="contact__icon" viewBox="0 0 26 26"><rect width="26" height="26" rx="5" fill="#b7966a"/><rect x="6" y="8" width="14" height="10" fill="none" stroke="#0d0d0e" stroke-width="2"/><path d="M6 8l7 6 7-6" fill="none" stroke="#0d0d0e" stroke-width="2"/></svg>
        youremail@mailbox.com
      </li>
      <li class="contact__item">
        <svg class="contact__icon" viewBox="0 0 26 26"><rect width="26" height="26" rx="5" fill="#b7966a"/><circle cx="13" cy="13" r="7" fill="none" stroke="#0d0d0e" stroke-width="2"/><path d="M6 13h14M13 6c-4 4-4 10 0 14M13 6c4 4 4 10 0 14" fill="none" stroke="#0d0d0e" stroke-width="1.5"/></svg>
        www.yourwebsite.com
      </li>
    </ul>
  </div>
</section>

</body>
</html>
```